Service and Repair for Motorize Wheelchairs

This is a new company and we are servicing and repairing motorized wheel chairs and other medical equipment. The company colors are red & white. I would like a picture of a motorized wheelchair faded in the back ground or at the end of the slogan, powerless. Add the email , rollingbaymedical@mailvane.com

The company name is Rolling Bay Medical, LLC

Industry/Entity Type

Medical

Contact Information for Business Card

Rolling Bay Medical, LLC
rolling forward with repair and support for every journey.
Curtis Lamble Owner
812 Harrow Crest Ct
Millbrook GA 30274
Office: 770-513-2967
Fax : 1855-394-2178
Cell: 770-381-6624

Font styles to use
Sans Serif

Colors
eb1f27
ffffff
000000

```html
<!DOCTYPE html>
<html lang="en">
<head>
<meta charset="utf-8">
<title>Rolling Bay Medical, LLC — Business Card</title>
<link rel="stylesheet" href="https://fonts.googleapis.com/css2?family=Archivo+Narrow:wght@700&family=Roboto:wght@300;400&display=swap">
<style>
  :root {
    --ink: #231f20;
    --brand-red: #eb1f27;
    --white: #ffffff;
    --chair-tone: #f2686d;
  }
  * { margin: 0; padding: 0; box-sizing: border-box; }
  html, body {
    width: 1200px;
    height: 702px;
    overflow: hidden;
    background: var(--white);
  }
  .card {
    position: relative;
    width: 1200px;
    height: 702px;
    display: flex;
  }
  .card__contact {
    position: relative;
    width: 581px;
    height: 100%;
    background: var(--ink);
    color: var(--white);
  }
  .company-name {
    position: absolute;
    left: 67px;
    top: 86px;
    font-family: "Archivo Narrow", "Arial Narrow", sans-serif;
    font-weight: 700;
    font-size: 40px;
    letter-spacing: 0.2px;
    white-space: nowrap;
  }
  .contact-list {
    position: absolute;
    left: 67px;
    top: 378px;
    list-style: none;
    font-family: "Roboto", Arial, sans-serif;
    font-weight: 400;
    font-size: 26px;
    line-height: 36.7px;
    white-space: nowrap;
  }
  .card__tagline-side {
    position: relative;
    flex: 1;
    height: 100%;
    background: var(--brand-red);
    color: var(--white);
  }
  .slogan {
    position: absolute;
    left: 50px;
    top: 86px;
    font-family: "Roboto", Arial, sans-serif;
    font-weight: 300;
    font-size: 43px;
    line-height: 45px;
    white-space: nowrap;
  }
  .chair-art {
    position: absolute;
    left: 210px;
    top: 228px;
    width: 330px;
    height: 430px;
  }
</style>
</head>
<body>
  <main class="card">
    <section class="card__contact">
      <h1 class="company-name">Rolling Bay Medical, LLC</h1>
      <ul class="contact-list">
        <li>Curtis Lamble Owner</li>
        <li>812 Harrow Crest Ct Millbrook</li>
        <li>GA 30274</li>
        <li>Office: 770-513-2967</li>
        <li>Fax : 1855-394-2178</li>
        <li>Cell: 770-381-6624</li>
        <li>rollingbaymedical@mailvane.com</li>
      </ul>
    </section>
    <section class="card__tagline-side">
      <p class="slogan">rolling forward with<br>repair and support<br>for every journey</p>
      <svg class="chair-art" role="img" aria-label="Faded wireframe illustration of a motorized wheelchair" viewBox="0 0 330 430">
        <defs>
          <radialGradient id="chairGlow" cx="50%" cy="55%" r="60%">
            <stop offset="0%" stop-color="var(--chair-tone)" stop-opacity="0.85"/>
            <stop offset="100%" stop-color="var(--chair-tone)" stop-opacity="0.15"/>
          </radialGradient>
        </defs>
        <rect width="330" height="430" rx="40" fill="url(#chairGlow)"/>
      </svg>
    </section>
  </main>
</body>
</html>
```